Startup online payment business - Sporting / Golf, Swift Tee payment

Background:
Our business name is "Swift Tee" we provide online payments for golfing services via our website. We currently have a logo used on our website. No other design style has been developed. Our aim is to remove cash payments for service at golf clubs.

Our Key Values:
Quick and easy
Formal and polite
Fun with professional boundary
Mate-ship relationships
100% online digital

What we want from you:
Marketing design to be used on posters and stickers in a retail setting to direct customers to our online payment Chanel.
Design must incorporate attached logo, URL swifttee.com.au and our key values can act as a guide the type of design. We have used color Hex#007672 for logo background. We are open to use other colors.

Target Market(s)

Golf clubs and golf players

Industry/Entity Type

Golf Course

Font styles to use
Sans Serif

Requirements
Must have
• Directions to online payment via URL: swifttee.com.au
Nice to have
• We like the idea of the slogan: No Cash - No worries. Have attached home screen that will be available from URL link. Consideration if using mobile phone in image. Push the online payment and steps 1. Visit swifttee.com 2. Select club 3. Confirm payment
Should not have
• Cartoons

```html
<!DOCTYPE html>
<html lang="en">
<head>
<meta charset="utf-8">
<title>Swift Tee – No Cash No Worries</title>
<link rel="stylesheet" href="https://fonts.googleapis.com/css2?family=Archivo+Black&family=Barlow+Condensed:wght@500;600&family=Barlow+Semi+Condensed:wght@600&display=swap">
<style>
  :root {
    --surround: #231f20;
    --teal: #117b73;
    --navy: #17284a;
    --orange: #f26522;
    --orange-deep: #ef4123;
    --white: #ffffff;
    --grass-top: #1f6b3c;
    --grass-bottom: #0f3b20;
  }
  * { margin: 0; padding: 0; box-sizing: border-box; }
  html, body { width: 900px; height: 1200px; overflow: hidden; background: var(--surround); }
  .canvas { position: relative; width: 900px; height: 1200px; background: var(--surround); }
  .poster {
    position: absolute; left: 88px; top: 88px; width: 724px; height: 1024px;
    background: var(--navy); overflow: hidden;
  }
  .poster-shapes { position: absolute; inset: 0; }
  .brand {
    position: absolute; left: 60px; top: 48px; width: 270px;
    font-family: "Barlow Condensed", sans-serif; font-weight: 500;
    font-size: 72px; letter-spacing: 6px; color: var(--white);
    text-align: center; line-height: 1;
  }
  .headline {
    position: absolute; left: 30px; top: 312px;
    font-family: "Barlow Condensed", sans-serif; font-weight: 600;
    color: var(--white); line-height: 1;
  }
  .headline-line { display: block; font-size: 108px; letter-spacing: -1px; }
  .headline .accent { color: var(--orange); }
  .headline-wide {
    display: block; font-family: "Archivo Black", sans-serif;
    font-size: 82px; color: var(--orange); line-height: 0.9;
    transform: scaleX(1.55); transform-origin: left center;
    letter-spacing: -2px; margin: 6px 0 8px;
  }
  .values {
    position: absolute; left: 392px; top: 706px; list-style: none;
    font-family: "Barlow Semi Condensed", sans-serif; font-weight: 600;
    font-size: 26px; line-height: 36px; color: var(--white);
  }
  .values li { position: relative; padding-left: 46px; }
  .values li::before {
    content: ""; position: absolute; left: 0; top: 10px;
    width: 38px; height: 20px; background: var(--orange);
    clip-path: polygon(0 0, 100% 0, 35% 100%);
  }
  .site-link {
    position: absolute; left: 0; right: 0; top: 968px; text-align: center;
    font-family: "Barlow Semi Condensed", sans-serif; font-weight: 600;
    font-size: 29px; color: var(--white); padding-left: 130px;
  }
</style>
</head>
<body>
<div class="canvas">
  <div class="poster">
    <svg class="poster-shapes" width="724" height="1024" viewBox="0 0 724 1024">
      <defs>
        <linearGradient id="orangeGrad" x1="0" y1="0" x2="1" y2="1">
          <stop offset="0" stop-color="#f7941d"/>
          <stop offset="1" stop-color="#ef4123"/>
        </linearGradient>
        <radialGradient id="photoGrad" cx="0.5" cy="0.45" r="0.6">
          <stop offset="0" stop-color="#eef0f3"/>
          <stop offset="0.55" stop-color="#c9d6ea"/>
          <stop offset="1" stop-color="#8fa6cf"/>
        </radialGradient>
        <linearGradient id="clubGrad" x1="0" y1="0" x2="0" y2="1">
          <stop offset="0" stop-color="#0f6a5f" stop-opacity="0.2"/>
          <stop offset="1" stop-color="#1a8a7c" stop-opacity="0.9"/>
        </linearGradient>
        <linearGradient id="grassGrad" x1="0" y1="0" x2="0" y2="1">
          <stop offset="0" stop-color="var(--grass-top)" stop-opacity="0"/>
          <stop offset="0.45" stop-color="var(--grass-top)"/>
          <stop offset="1" stop-color="var(--grass-bottom)"/>
        </linearGradient>
      </defs>
      <polygon class="band-top" points="0,0 596,0 248,248 0,212" fill="var(--teal)"/>
      <polygon class="band-bottom" points="0,868 470,622 724,660 724,1024 0,1024" fill="var(--teal)"/>
      <g role="img" aria-label="Golf club striking a ball on a tee">
        <rect x="120" y="560" width="260" height="400" fill="url(#clubGrad)" opacity="0.55" rx="20"/>
      </g>
      <rect role="img" aria-label="Grass strip" x="0" y="920" width="724" height="104" fill="url(#grassGrad)"/>
      <circle role="img" aria-label="Photo of a worried man looking into an empty wallet" cx="544" cy="408" r="250" fill="url(#photoGrad)"/>
      <circle cx="544" cy="408" r="252" fill="none" stroke="url(#orangeGrad)" stroke-width="18"/>
      <polygon points="350,192 408,156 462,260" fill="url(#orangeGrad)"/>
      <polygon points="300,636 424,584 392,676" fill="url(#orangeGrad)"/>
    </svg>

    <div class="brand">SWIFT TEE</div>

    <h1 class="headline">
      <span class="headline-line"><span class="accent">NO</span>CASH<span class="accent">!</span></span>
      <span class="headline-wide">NO</span>
      <span class="headline-line">WORRIES</span>
    </h1>

    <ul class="values">
      <li>Quick and easy</li>
      <li>Formal and polite</li>
      <li>Fun with professional<br>boundary</li>
      <li>Mate-ship relationships</li>
      <li>100% online digital</li>
    </ul>

    <p class="site-link">Visit: www.swifttee.com.au</p>
  </div>
</div>
</body>
</html>
```